Online Travel Agency card design with 2 logos

Need a two sided business card design for online tourism agency which is based in Istanbul Turkey.
Need a business card design where it shows the travel agency logo but also the logo and information of the parent company as well.Parent company logo is just text with 2 different colors. (Arial font with text TemaVista "Tema"- hex #172841 and "Vista" hex-#FF7F00)
Both logos are uploaded.
Target Market(s)
travel , online
Industry/Entity Type
Travel
Contact Information for Business Card
The information on the card should be as :
Travel Agency Logo logo (rnlogo)
Parent Company logo(temalogo)
Company information :TemaVista Turizm ve Bilgi Teknolojileri A.Ş
Address of company
Tel
Email
Name
Position(english and turkish)
Look and feel
Each slider illustrates characteristics of the customer's brand and the style your logo design should communicate.

```html
<!DOCTYPE html>
<html lang="tr">
<head>
<meta charset="utf-8">
<title>Rotanova – TemaVista business card</title>
<link rel="stylesheet" href="https://fonts.googleapis.com/css2?family=Roboto:wght@400;500;700&display=swap">
<style>
  :root {
    --backdrop: #2a2a2c;
    --card-white: #ffffff;
    --navy: #172841;
    --sky: #6fcbe8;
    --orange: #ff7f00;
    --pattern-light: #f4f5f7;
    --pattern-mid: #e6e8ec;
  }
  * { box-sizing: border-box; margin: 0; padding: 0; }
  html, body { width: 1200px; height: 852px; overflow: hidden; }
  body {
    background: var(--backdrop);
    font-family: "Roboto", Arial, sans-serif;
    display: flex; align-items: center; justify-content: center; gap: 40px;
  }
  .card {
    position: relative; width: 540px; height: 310px;
    border-radius: 22px; overflow: hidden; background: var(--card-white);
    box-shadow: 0 14px 30px rgba(0,0,0,.45);
  }
  /* Front */
  .front-texture {
    position: absolute; inset: 0;
    background: radial-gradient(circle at 50% 50%, var(--pattern-light), var(--pattern-mid));
  }
  .front-brand {
    position: absolute; left: 0; right: 0; top: 50%; transform: translateY(-50%);
    text-align: center;
    font-size: 50px; font-weight: 700; color: var(--navy); letter-spacing: -0.5px;
  }
  /* Back */
  .back-shapes { position: absolute; inset: 0; width: 100%; height: 100%; }
  .back-brands {
    position: absolute; left: 26px; top: 88px;
    display: flex; align-items: baseline; gap: 28px;
    color: var(--navy); font-weight: 700;
  }
  .agency-name { font-size: 26px; }
  .parent-name { font-size: 26px; }
  .company-line {
    position: absolute; left: 26px; top: 132px;
    font-size: 16px; font-weight: 500; color: var(--navy);
  }
  .person { position: absolute; left: 26px; top: 216px; color: #fff; }
  .person-name { font-size: 17px; font-weight: 700; }
  .person-role { font-size: 11px; color: var(--orange); line-height: 1.3; margin-top: 2px; }
  .person-address { font-size: 11px; line-height: 1.4; margin-top: 5px; }
  .contact {
    position: absolute; left: 290px; top: 222px; list-style: none;
    color: #fff; font-size: 11px; line-height: 1.7;
  }
  .contact li { display: flex; align-items: center; gap: 6px; }
  .contact svg { width: 12px; height: 12px; flex: none; }
</style>
</head>
<body>
  <section class="card card-front" aria-label="Card front">
    <div class="front-texture" role="img" aria-label="Faint repeating brand pattern"></div>
    <p class="front-brand">Rotanova</p>
  </section>

  <section class="card card-back" aria-label="Card back">
    <svg class="back-shapes" viewBox="0 0 540 310" preserveAspectRatio="none" aria-hidden="true">
      <path fill="var(--orange)" d="M395,0 L470,0 C468,40 458,75 445,100 C430,60 415,28 395,0 Z"/>
      <path fill="var(--sky)" d="M0,192 C120,152 260,182 360,162 C420,150 458,105 470,0 L500,0 C482,120 432,168 360,182 C260,202 120,172 0,212 Z"/>
      <path fill="var(--navy)" d="M0,212 C120,172 260,202 360,182 C432,168 482,120 500,0 L540,0 L540,310 L0,310 Z"/>
    </svg>

    <div class="back-brands">
      <span class="agency-name">Rotanova</span>
      <span class="parent-name">TemaVista</span>
    </div>
    <p class="company-line">TemaVista Turizm ve Bilgi Teknolojileri A.Ş</p>

    <div class="person">
      <p class="person-name">Derya Aksoy</p>
      <p class="person-role">Managing Director<br>Genel müdür</p>
      <p class="person-address">2210 Harbor Lane Unit 400<br>Lakeview, IL 60420</p>
    </div>

    <ul class="contact">
      <li>
        <svg viewBox="0 0 12 12"><rect x="0.5" y="0.5" width="11" height="11" rx="2" fill="none" stroke="#fff"/><path d="M3.5,2.8 C3,5.5 6,8.8 9,8.5 L9,7.2 L7.6,6.7 L6.9,7.4 C5.9,7 4.9,6 4.6,5.1 L5.3,4.4 L4.8,2.8 Z" fill="#fff"/></svg>
        0733-555-214
      </li>
      <li>
        <svg viewBox="0 0 12 12"><rect x="0.5" y="0.5" width="11" height="11" rx="2" fill="#fff"/><rect x="2.5" y="3.5" width="7" height="5" fill="none" stroke="var(--navy)"/><path d="M2.5,3.5 L6,6.3 L9.5,3.5" fill="none" stroke="var(--navy)"/></svg>
        d.aksoy@temavista.com
      </li>
    </ul>
  </section>
</body>
</html>
```